new marketing company logo and business card

design logo and biz card for marketing start up.

My company name needs a brand logo designed: Cedar Hollow Marketing Co.
Tagline: Sales - Marketing - Brand Building

Sister Bay is the name of my favorite place, in Wisconsin, but the business is NOT BASED there. It should evoke warmth, friendliness, professionalism, and marketing services from a seasoned marketer.

Target Market(s)

I am selling my services to small business that need help.

Industry/Entity Type

Marketing

Contact Information for Business Card

Cedar Hollow Marketing Co. (logo)
Sales - Marketing - Brand Building (tagline)

Maren T. Holloway
MarenTHolloway@quillpost.net
555-014-3926 mobile

Font styles to use
Serif
Sans Serif

Colors
f78f20
f37122
f68d4d
00a990
85cae6
33b8a4
faa54b

Requirements
Must have
• a logo
• a business card
Nice to have
• I'd love to see a small subtle reference to Sister Bay built in. Sister bay is named that because there are two islands called ‘sister islands’ that flank the bay. If you google this you will see.
• I like warm, earthy colors. But, I am a fun, approachable, real person. Not stand-offish. Should be warm and appealing yet professional.
Should not have
• nothing cartoon-ish. no child-like fonts. this is a professional business.

```html
<!DOCTYPE html>
<html lang="en">
<head>
<meta charset="utf-8">
<title>Cedar Hollow Marketing Co. — Business Card</title>
<link href="https://fonts.googleapis.com/css2?family=Inter:wght@400;500;600&display=swap" rel="stylesheet">
<style>
  :root {
    --backdrop: #e1e1e1;
    --card: #ffffff;
    --teal: #14ab91;
    --orange: #f37122;
    --ink: #5a5a5a;
  }
  * { margin: 0; padding: 0; box-sizing: border-box; }
  html, body { width: 1200px; height: 1200px; overflow: hidden; }
  body {
    background: var(--backdrop);
    font-family: "Inter", "Helvetica Neue", Arial, sans-serif;
    position: relative;
  }
  .card {
    position: absolute;
    left: 156px;
    width: 889px;
    height: 511px;
    background: var(--card);
    box-shadow: 0 1px 5px rgba(0,0,0,0.22);
  }
  .card--front { top: 62px; }
  .card--back { top: 630px; }

  .brand-frame {
    position: absolute;
    left: 194px; top: 73px;
    width: 518px; height: 301px;
    border: 2.5px solid var(--teal);
  }
  .brand-mark {
    position: absolute;
    left: 389px; top: 114px;
    width: 129px; height: 115px;
    background: var(--teal);
  }
  .brand-name {
    position: absolute;
    left: 0; right: 0; top: 244px;
    text-align: center;
    color: var(--teal);
    font-weight: 400;
    font-size: 42px;
    line-height: 42px;
    letter-spacing: 0.16em;
    text-indent: 0.16em;
  }
  .tagline {
    position: absolute;
    left: 0; right: 0; top: 428px;
    text-align: center;
    color: var(--orange);
    font-weight: 600;
    font-size: 25px;
    letter-spacing: 0.13em;
  }

  .contact-frame {
    position: absolute;
    left: 54px; top: 52px;
    width: 780px; height: 406px;
    border: 2.5px solid var(--teal);
  }
  .person-name {
    position: absolute;
    left: 236px; top: 160px;
    color: var(--orange);
    font-weight: 600;
    font-size: 42px;
    letter-spacing: 0.05em;
  }
  .contact-row {
    position: absolute;
    left: 236px;
    display: flex;
    align-items: center;
    gap: 14px;
  }
  .contact-row--phone { top: 235px; }
  .contact-row--email { top: 292px; }
  .contact-icon {
    width: 48px; height: 48px;
    border-radius: 14px;
    background: var(--teal);
    display: flex; align-items: center; justify-content: center;
  }
  .contact-text {
    color: var(--ink);
    font-size: 23px;
    letter-spacing: 0.06em;
  }
</style>
</head>
<body>
  <section class="card card--front">
    <div class="brand-frame"></div>
    <div class="brand-mark"></div>
    <h1 class="brand-name">CEDAR HOLLOW<br>MARKETING CO</h1>
    <p class="tagline">SALES - MARKETING - BRAND BUILDING</p>
  </section>

  <section class="card card--back">
    <div class="contact-frame"></div>
    <h2 class="person-name">Maren T. Holloway</h2>
    <div class="contact-row contact-row--phone">
      <span class="contact-icon">
        <svg width="28" height="28" viewBox="0 0 24 24" aria-hidden="true">
          <path fill="#fff" d="M6.6 10.8c1.4 2.8 3.8 5.1 6.6 6.6l2.2-2.2c.3-.3.7-.4 1-.2 1.1.4 2.3.6 3.6.6.6 0 1 .4 1 1V20c0 .6-.4 1-1 1C10.6 21 3 13.4 3 4c0-.6.4-1 1-1h3.5c.6 0 1 .4 1 1 0 1.3.2 2.5.6 3.6.1.3 0 .7-.2 1z"/>
        </svg>
      </span>
      <span class="contact-text">555-014-3926</span>
    </div>
    <div class="contact-row contact-row--email">
      <span class="contact-icon">
        <svg width="32" height="22" viewBox="0 0 32 22" aria-hidden="true">
          <rect x="1.5" y="1.5" width="29" height="19" fill="none" stroke="#fff" stroke-width="2.5"/>
          <path d="M1.5 1.5 L16 12 L30.5 1.5 M1.5 20.5 L12 10 M30.5 20.5 L20 10" fill="none" stroke="#fff" stroke-width="2.2"/>
        </svg>
      </span>
      <span class="contact-text">MarenTHolloway@quillpost.net</span>
    </div>
  </section>
</body>
</html>
```